Window Cleaning Leaflet

Hi everyone,

I need a leaflet (couldn't find 'leaflet' as an option when begining this project - so one sided only) to send out to coastal properties in South side Melbourne. The Flyer is aimed at high net individuals, mummies, business people etc who own these properties who don't have time to clean the windows themselves (often multiple levels) and want their home looking fabulous in time for Christmas and NY's celebrations.

I would really love a new and original design for a window washing leaflet. something outside of the norm that 'pops' and makes people feel happy when they look at it.

I guess a point of differentiation is that I'm a female working in a mans industry so appeal to mothers looking for someone who is 'reliable, trustworthy and understanding of peoples needs'.

I have made an outline of what I would like included in the leaflet, so if you could please take a look, feel free to change things around, wording and layout etc. If you can make it sound more professional please do so.

I would like the colours to be 'happy' colours, maybe with a silly season theme?

Overall aesthetically pleasing is a must, I find most window cleaning leaflets fairly mundane and boring, please feel free to think outside the box. The more original the better.

Target Market(s)

People who own large Melbourne homes in affluent suburbs, mainly suburbs with a lot of large coastal properties. Generally owned by high net worth individuals who just don't have tme to clean the windows themselves due to their profession or hectic lifestyles but can afford to pay someone else to do it.

Industry/Entity Type

Window Cleaning

Requirements
Must have
• 1) The name of the business - Tilda’s Glass Gleaming Services
• 2) The coupon special and all details attached:
• Small Homes (up to 12 windows) $120
• Medium Homes (up to 16 windows) $180
• Large Homes (up to 20 windows, 2 storeys) $240
• 20% discount
• *Discount applicable to first time customers only.
• *All services include fly screen, sill and tracks cleaned as well as cobweb removal.
• *Houses with more than 20 windows (or two levels) will have an immediate quote provided upon inspection of the property with 20% discount applied.
• *Tilda’s Glass Gleaming Services are fully insured.
• 3) My contact number - 0418 263 591

```html
<!DOCTYPE html>
<html lang="en">
<head>
<meta charset="utf-8">
<title>Tilda’s Glass Gleaming Services – Leaflet</title>
<link href="https://fonts.googleapis.com/css2?family=Anton&family=Arimo:wght@400;700&display=swap" rel="stylesheet">
<style>
  :root {
    --brand-blue: #1d74b8;
    --deep-blue: #175f9c;
    --band-blue: #1a6aab;
    --sky-light: #e6f2fb;
    --sky-mid: #b9dcf3;
    --leaf-green: #7cb83a;
    --ink: #111111;
    --sparkle-red: #e2231a;
    --white: #ffffff;
    --stage: #eef1f4;
  }
  * { box-sizing: border-box; margin: 0; padding: 0; }
  html, body { width: 1200px; height: 1000px; overflow: hidden; }
  body { background: var(--stage); font-family: "Arimo", Arial, sans-serif; }

  .leaflet {
    position: absolute; left: 260px; top: 20px;
    width: 680px; height: 960px;
    background: linear-gradient(180deg, var(--white) 0%, var(--sky-light) 30%, var(--white) 80%);
    overflow: hidden;
    box-shadow: 0 4px 18px rgba(0,0,0,.18);
  }
  .leaflet > * { position: absolute; }

  .top-swoosh { left: 0; top: 0; width: 680px; height: 320px; }

  .hero-photo {
    left: 60px; top: 230px; width: 560px; height: 420px;
    background: radial-gradient(ellipse at 60% 35%, #ffffff 0%, #d4eaf8 45%, #a9d1ee 100%);
    border-radius: 6px;
    opacity: .95;
  }

  .business-name { left: 28px; top: 18px; font-family: "Anton", Impact, sans-serif; line-height: 1; }
  .business-name .lead { display: flex; align-items: baseline; gap: 12px; color: var(--brand-blue); }
  .business-name .first { font-size: 112px; letter-spacing: -1px; }
  .business-name .second { font-size: 62px; }
  .business-name .rest { color: var(--leaf-green); font-size: 80px; margin-top: -6px; display: block; }

  .discount-badge { left: 500px; top: 250px; width: 150px; height: 150px; }

  .question { left: 36px; top: 325px; font-family: "Anton", Impact, sans-serif; font-size: 34px; line-height: 1.05; transform: rotate(-3deg); }
  .question .q1 { color: var(--brand-blue); display: block; }
  .question .q2 { color: var(--ink); display: block; padding-left: 6px; }

  .busy-parent {
    left: 420px; top: 455px; width: 230px;
    font-weight: 700; font-size: 21px; line-height: 1.25; text-align: center; color: var(--ink);
    transform: rotate(-3deg);
  }

  .pitch {
    left: 60px; top: 600px; width: 600px;
    font-size: 25px; line-height: 1.3; text-align: center; color: var(--ink);
    transform: rotate(-3deg);
  }
  .pitch .reliable { color: var(--leaf-green); font-weight: 700; }
  .pitch .professional { color: var(--brand-blue); font-weight: 700; }
  .pitch .sparkle { color: var(--sparkle-red); font-weight: 700; }

  .call-to-action {
    left: 110px; top: 718px; width: 520px;
    font-size: 20px; line-height: 1.3; text-align: center; color: var(--brand-blue);
    transform: rotate(-3deg);
  }

  .phone-line {
    left: 200px; top: 778px; width: 420px;
    font-family: "Anton", Impact, sans-serif; font-size: 38px; color: var(--deep-blue); text-align: center;
    transform: rotate(-3deg);
  }

  .offer-band { left: 0; top: 820px; width: 680px; height: 140px; }

  .price-table { left: 34px; top: 862px; width: 240px; color: var(--white); border-collapse: collapse; }
  .price-table td { padding: 3px 0; border-bottom: 1px solid rgba(255,255,255,.35); vertical-align: middle; }
  .price-table tr:last-child td { border-bottom: none; }
  .price-table .size { font-weight: 700; font-size: 14px; line-height: 1.05; }
  .price-table .size small { display: block; font-weight: 400; font-size: 9px; }
  .price-table .price { font-weight: 700; font-size: 22px; text-align: right; }

  .fine-print {
    left: 320px; top: 856px; width: 340px;
    list-style: none; color: var(--white); font-size: 9.5px; line-height: 1.25;
  }
</style>
</head>
<body>
<main class="leaflet">
  <svg class="top-swoosh" viewBox="0 0 680 320" aria-hidden="true">
    <defs>
      <linearGradient id="swooshBlue" x1="0" y1="0" x2="1" y2="1">
        <stop offset="0" stop-color="#ffffff"/>
        <stop offset="1" stop-color="#9fd0f0"/>
      </linearGradient>
    </defs>
    <path d="M0 0 H680 V260 C560 200 420 230 300 200 C180 170 80 200 0 170 Z" fill="#ffffff"/>
    <path d="M360 120 C460 80 580 110 680 70 V170 C580 200 470 160 360 120 Z" fill="url(#swooshBlue)" opacity=".55"/>
  </svg>

  <div class="hero-photo" role="img" aria-label="Photo of a woman cleaning a bright window with a long-handled squeegee against a blue sky"></div>

  <h1 class="business-name">
    <span class="lead"><span class="first">Tilda’s</span><span class="second">Glass</span></span>
    <span class="rest">Gleaming Services</span>
  </h1>

  <svg class="discount-badge" viewBox="0 0 150 150" role="img" aria-label="20% discount">
    <circle cx="75" cy="72" r="66" fill="var(--brand-blue)" stroke="#ffffff" stroke-width="4"/>
    <path d="M60 132 L52 148 L78 136 Z" fill="var(--brand-blue)"/>
    <text x="75" y="82" text-anchor="middle" font-family="Anton, Impact, sans-serif" font-size="50" fill="#ffffff">20%</text>
    <text x="75" y="108" text-anchor="middle" font-family="Anton, Impact, sans-serif" font-size="20" fill="#ffffff">Discount</text>
  </svg>

  <p class="question"><span class="q1">Do you need your</span><span class="q2">windows cleaned?</span></p>

  <p class="busy-parent">Are you simply too busy as a hard working parent to do it yourself?</p>

  <p class="pitch">Tilda’s Glass Gleaming Services provide a <span class="reliable">reliable,</span> <span class="professional">professional service,</span> ensuring that your home will <span class="sparkle">sparkle.</span></p>

  <p class="call-to-action">Call Tilda today and take advantage of our special introductory offer.</p>

  <p class="phone-line">Tilda - 0418 263 591</p>

  <svg class="offer-band" viewBox="0 0 680 140" aria-hidden="true">
    <path d="M0 34 C200 20 450 10 680 0 V140 H0 Z" fill="var(--band-blue)"/>
  </svg>

  <table class="price-table">
    <tr><td class="size">Small Homes<small>(up to 12 windows)</small></td><td class="price">$120</td></tr>
    <tr><td class="size">Medium Homes<small>(up to 16 windows)</small></td><td class="price">$180</td></tr>
    <tr><td class="size">Large Homes<small>(up to 20 windows, 2 storeys)</small></td><td class="price">$240</td></tr>
  </table>

  <ul class="fine-print">
    <li>*Discount applicable to first time customers only.</li>
    <li>*All services include fly screen, sill and tracks cleaned as well as cobweb removal.</li>
    <li>*Houses with more than 20 windows (or two levels) will have an immediate quote provided upon inspection of the property with 20% discount applied.</li>
    <li>*Tilda’s Glass Gleaming Services are fully insured.</li>
  </ul>
</main>
</body>
</html>
```